Redesign of business card for Birchline Mechanical

We are looking for a new design for our business cards for Birchline Mechanical. We are a plumbing & HVAC construction company, operating on the West Coast of Canada and USA. Logo attached.
Industry/Entity Type
Construction - Plumbing & HVAC
Contact Information for Business Card
Name, address, phone numbers, email, website address
Look and feel
Each slider illustrates characteristics of the customer's brand and the style your logo design should communicate.

```html
<!DOCTYPE html>
<html lang="en">
<head>
<meta charset="utf-8">
<title>Birchline Mechanical – Business Card</title>
<link href="https://fonts.googleapis.com/css2?family=Jost:wght@400;500;700&display=swap" rel="stylesheet">
<style>
  :root {
    --bg: #e4e5e7;
    --ink: #1c1c1c;
    --muted: #8a8a8a;
    --rule: #b9b9b9;
    --paper: #ffffff;
    --steel-dark: #8f9092;
    --steel-mid: #c4c5c7;
    --steel-light: #f1f1f2;
  }
  * { margin: 0; padding: 0; box-sizing: border-box; }
  html, body { width: 1200px; height: 800px; overflow: hidden; }
  body {
    background: var(--bg);
    font-family: "Jost", "Futura", sans-serif;
    color: var(--ink);
    position: relative;
  }
  .card {
    position: absolute;
    top: 245px;
    width: 540px;
    height: 309px;
    box-shadow: 0 6px 18px rgba(0,0,0,0.18);
    overflow: hidden;
  }

  /* Back side – services */
  .card-back {
    left: 40px;
    background: linear-gradient(100deg,
      var(--steel-dark) 0%, var(--steel-mid) 18%, var(--steel-light) 32%,
      var(--steel-mid) 44%, var(--steel-dark) 52%, var(--steel-light) 66%,
      var(--steel-mid) 80%, var(--steel-light) 92%, var(--steel-mid) 100%);
  }
  .services {
    position: absolute;
    left: 34px;
    top: 118px;
  }
  .services-heading {
    display: flex;
    align-items: center;
    font-weight: 700;
    font-size: 14px;
    letter-spacing: 0.02em;
    text-transform: uppercase;
    margin-bottom: 6px;
  }
  .services-heading::after {
    content: "";
    display: block;
    width: 100px;
    height: 1px;
    background: var(--ink);
    margin-left: 6px;
  }
  .services-list { list-style: none; }
  .services-list li {
    font-size: 13.5px;
    line-height: 21px;
    padding-left: 14px;
    position: relative;
  }
  .services-list li::before {
    content: "";
    position: absolute;
    left: 0;
    top: 7px;
    width: 7px;
    height: 7px;
    border-radius: 50%;
    background: var(--ink);
  }

  .brand {
    position: absolute;
    display: flex;
    align-items: center;
    gap: 10px;
    font-weight: 500;
    font-size: 20px;
    text-transform: uppercase;
    letter-spacing: 0.04em;
    color: var(--ink);
  }
  .brand-mark {
    width: 16px;
    height: 16px;
    background: var(--ink);
  }
  .card-back .brand { right: 30px; top: 44px; }

  /* Front side – contact */
  .card-front {
    left: 620px;
    background: var(--paper);
  }
  .card-front .brand { right: 30px; top: 66px; }
  .person {
    position: absolute;
    left: 30px;
    top: 30px;
  }
  .person-name {
    font-weight: 700;
    font-size: 15px;
    text-transform: uppercase;
    letter-spacing: 0.02em;
  }
  .person-title-row {
    display: flex;
    align-items: center;
    width: 260px;
  }
  .person-title {
    font-size: 12.5px;
    color: var(--muted);
  }
  .person-title-row::after {
    content: "";
    flex: 1;
    height: 1px;
    background: var(--rule);
    margin-left: 4px;
    margin-top: 6px;
  }
  .contact-list { list-style: none; margin-top: 2px; }
  .contact-list li {
    display: flex;
    align-items: center;
    gap: 6px;
    font-size: 13.5px;
    line-height: 19px;
  }
  .contact-list svg { width: 11px; height: 11px; flex: none; }
  .address-block {
    position: absolute;
    right: 30px;
    bottom: 30px;
    text-align: right;
    width: 300px;
  }
  .address-block::before {
    content: "";
    display: block;
    height: 1px;
    background: var(--rule);
    margin-bottom: 10px;
  }
  .address {
    font-style: normal;
    font-size: 13.5px;
    line-height: 18px;
  }
</style>
</head>
<body>

  <section class="card card-back" aria-label="Business card back">
    <div class="brand"><span class="brand-mark"></span>Birchline Mechanical</div>
    <div class="services">
      <h2 class="services-heading">Our Services</h2>
      <ul class="services-list">
        <li>Pipefitting Systems / Design Build</li>
        <li>Maintenance / Fire Protection / Control Systems</li>
        <li>Energy Recovery &amp; High Efficiency Systems</li>
        <li>Plumbing / HVAC</li>
      </ul>
    </div>
  </section>

  <section class="card card-front" aria-label="Business card front">
    <div class="person">
      <h1 class="person-name">Calvin Marsh</h1>
      <div class="person-title-row"><span class="person-title">President/Founder</span></div>
      <ul class="contact-list">
        <li>
          <svg viewBox="0 0 12 12" aria-hidden="true"><circle cx="6" cy="6" r="5.4" fill="none" stroke="#1c1c1c" stroke-width="1"/><path d="M4 3.2l1 .2.4 1.3-.6.5c.3.7.8 1.2 1.5 1.5l.5-.6 1.3.4.2 1c-.4.4-1 .6-1.5.4C5.3 7.5 4.5 6.7 4 5.2c-.2-.6 0-1.5 0-2z" fill="#1c1c1c"/></svg>
          604-555-0182
        </li>
        <li>
          <svg viewBox="0 0 12 12" aria-hidden="true"><rect x="0.8" y="2.5" width="10.4" height="7" fill="none" stroke="#1c1c1c" stroke-width="1"/><path d="M1 3l5 3.6L11 3" fill="none" stroke="#1c1c1c" stroke-width="1"/></svg>
          info@birchlinemech.com
        </li>
        <li>
          <svg viewBox="0 0 12 12" aria-hidden="true"><circle cx="6" cy="6" r="5.3" fill="none" stroke="#1c1c1c" stroke-width="1"/><ellipse cx="6" cy="6" rx="2.3" ry="5.3" fill="none" stroke="#1c1c1c" stroke-width="0.8"/><path d="M0.8 6h10.4M1.6 3.5h8.8M1.6 8.5h8.8" stroke="#1c1c1c" stroke-width="0.7"/></svg>
          www.birchlinemech.com
        </li>
      </ul>
    </div>
    <div class="brand"><span class="brand-mark"></span>Birchline Mechanical</div>
    <div class="address-block">
      <address class="address">2250 Harbor Line Rd.<br>Suite #114 Tacoma, WA 98421</address>
    </div>
  </section>

</body>
</html>
```